Emergency Medical Training and Events Company Business Needs Business Card Design

We are in need of a business card for our dynamic company expanding its customer base and need to be easily contacted and identified for when we visit with government officials, potential EMS / Fire agencies and county coordinators to arrange for training programs for first responders to better prepare them for critical thinking at critical incidents.
Updates

Need extra days to review

Target Market(s)

EMS/Fire and Event Promoters

Industry/Entity Type

Medical

Contact Information for Business Card

Two cards, comparable designs:

Gavin R. Thorley, Principal, g.thorley@vantrexmed.com
Neil Carrow, Event and Training Specialist, n.carrow@vantrexmed.com

Font styles to use
Other font styles liked:
• Cambria

Colors

Designer to choose colors to be used in the design.

Requirements
Must have
• Company Logo, Spots for Name, Title, Phone Number, Email, Website
• A bullet list stating that we offer, KMB CPR and First Aid Instructors, Hold the Line Instructors, Event EMS, CME's, MCI Training and Planning. We prefer to have a black background for the card but if you can make a blue or white card stand out we would review that as well.
Should not have
• Tacky logos or special sayings ... simple, elegant, professional is the look we seek

```html
<!DOCTYPE html>
<html lang="en">
<head>
<meta charset="utf-8">
<title>Vantrex Medical Business Cards</title>
<link href="https://fonts.googleapis.com/css2?family=Montserrat:wght@400;500;700&display=swap" rel="stylesheet">
<style>
  :root {
    --bg: #262626;
    --navy: #0f1d5e;
    --navy-soft: #16267a;
    --red: #d6202b;
    --white: #ffffff;
  }
  * { box-sizing: border-box; margin: 0; padding: 0; }
  html, body { width: 1200px; height: 900px; overflow: hidden; }
  body {
    background: var(--bg);
    font-family: "Montserrat", sans-serif;
    display: flex;
    flex-direction: column;
    align-items: center;
    justify-content: center;
    gap: 36px;
  }
  .card {
    position: relative;
    width: 720px;
    height: 400px;
    background: var(--navy);
    color: var(--white);
    overflow: hidden;
    box-shadow: 0 10px 30px rgba(0,0,0,.5);
  }
  .brand {
    display: flex;
    align-items: center;
    gap: 14px;
    white-space: nowrap;
  }
  .brand-mark {
    width: 54px; height: 54px;
    border-radius: 50%;
    background: var(--red);
    flex: none;
  }
  .brand-name {
    font-weight: 700;
    font-size: 30px;
    letter-spacing: 1px;
    line-height: 1;
    color: var(--white);
  }

  /* back side */
  .card-back .faint-circle {
    position: absolute;
    left: -60px; top: 40px;
    width: 300px; height: 300px;
    border-radius: 50%;
    background: var(--navy-soft);
    opacity: .45;
  }
  .card-back .brand {
    position: absolute;
    right: 50px; top: 70px;
  }
  .services {
    position: absolute;
    left: 330px; top: 215px;
    list-style: none;
    font-size: 17px;
    line-height: 1.32;
    letter-spacing: .5px;
    white-space: nowrap;
  }
  .services li { position: relative; padding-left: 20px; }
  .services li::before {
    content: "";
    position: absolute;
    left: 0; top: 7px;
    width: 9px; height: 9px;
    border-radius: 50%;
    background: var(--red);
  }

  /* front side */
  .card-front .brand {
    position: absolute;
    left: 50%; top: 52px;
    transform: translateX(-50%);
  }
  .person {
    position: absolute;
    left: 0; right: 0; top: 140px;
    text-align: center;
  }
  .person-name {
    font-weight: 500;
    font-size: 46px;
    letter-spacing: 3px;
    text-transform: uppercase;
    line-height: 1.05;
  }
  .person-title {
    font-size: 20px;
    color: var(--red);
    letter-spacing: .8px;
  }
  .divider {
    position: absolute;
    left: 60px; right: 60px; top: 272px;
    height: 2px;
    background: var(--red);
  }
  .contacts {
    position: absolute;
    left: 36px; right: 36px; top: 318px;
    display: flex;
    justify-content: space-between;
    align-items: center;
    font-size: 16px;
    letter-spacing: .3px;
    white-space: nowrap;
  }
  .contact { display: flex; align-items: center; gap: 8px; }
  .contact svg { width: 18px; height: 18px; flex: none; }
  .web-accent { color: var(--red); font-weight: 500; }
</style>
</head>
<body>
  <section class="card card-back">
    <div class="faint-circle" aria-hidden="true"></div>
    <div class="brand">
      <span class="brand-mark" aria-hidden="true"></span>
      <span class="brand-name">VANTREX MEDICAL</span>
    </div>
    <ul class="services">
      <li>KMB CPR and First Aid Instructors</li>
      <li>Hold the Line Instructors</li>
      <li>Event EMS</li>
      <li>CME's</li>
      <li>MCI Training and Planning</li>
    </ul>
  </section>

  <section class="card card-front">
    <div class="brand">
      <span class="brand-mark" aria-hidden="true"></span>
      <span class="brand-name">VANTREX MEDICAL</span>
    </div>
    <div class="person">
      <h1 class="person-name">Neil Carrow</h1>
      <p class="person-title">Event and Training Specialist</p>
    </div>
    <div class="divider"></div>
    <div class="contacts">
      <div class="contact">
        <svg viewBox="0 0 24 24" fill="none" stroke="#d6202b" stroke-width="2" aria-hidden="true">
          <path d="M5 3h4l2 5-2.5 1.5a11 11 0 0 0 6 6L16 13l5 2v4a2 2 0 0 1-2 2A16 16 0 0 1 3 5a2 2 0 0 1 2-2z"/>
        </svg>
        <span>123.456.7890</span>
      </div>
      <div class="contact">
        <svg viewBox="0 0 24 24" fill="none" stroke="#d6202b" stroke-width="2" aria-hidden="true">
          <rect x="2" y="5" width="20" height="14"/><path d="M2 5l10 8 10-8"/>
        </svg>
        <span>n.carrow@vantrexmed.com</span>
      </div>
      <div class="contact">
        <svg viewBox="0 0 24 24" fill="none" stroke="#d6202b" stroke-width="2" aria-hidden="true">
          <circle cx="12" cy="12" r="10"/><path d="M2 12h20M12 2a15 15 0 0 1 0 20M12 2a15 15 0 0 0 0 20"/>
        </svg>
        <span>www.<span class="web-accent">vantrexmed</span>.com</span>
      </div>
    </div>
  </section>
</body>
</html>
```